Company or website name
- Harwood & Beale LLP
- Links to the website
- harwoodbeale-example.com
- Describe your company and organization and target audience
- lawyers and clients in the need of lawyer for defective products etc
- The design should have the following
- yes
- Other Facts

```html
<!DOCTYPE html>
<html lang="en">
<head>
<meta charset="utf-8">
<title>Harwood &amp; Beale LLP</title>
<link rel="stylesheet" href="https://fonts.googleapis.com/css2?family=Noticia+Text:wght@400;700&family=Open+Sans:wght@400;600&display=swap">
<style>
:root{
  --blue:#1b86d6;
  --blue-light:#3aa6ec;
  --green:#5a9a3c;
  --green-btn:#6aa352;
  --dark:#2b2b2b;
  --header:rgba(30,28,26,.85);
  --text:#444;
  --muted:#777;
  --rule:#dcdcdc;
  --band:#f2f2f2;
  --white:#fff;
}
*{box-sizing:border-box;margin:0;padding:0}
html,body{width:1200px;height:2514px;overflow:hidden}
body{position:relative;background:var(--white);font-family:"Open Sans",sans-serif;color:var(--text)}
.abs{position:absolute}
.serif{font-family:"Noticia Text",serif}

/* hero */
.hero-photo{left:0;top:0;width:1200px;height:648px;background:linear-gradient(100deg,#9a8a74 0%,#c9b9a3 25%,#d8cdbd 40%,#5a534c 60%,#3b3733 80%,#7d6f60 100%)}
.header{left:0;top:0;width:1200px;height:88px;background:var(--header)}
.brand{left:177px;top:20px;font-family:"Noticia Text",serif;font-size:29px;color:var(--white)}
.social{left:935px;top:33px;display:flex;gap:10px}
.social span{width:14px;height:14px;border-radius:50%;background:var(--white)}
.nav{left:174px;top:78px;width:848px;height:49px;background:var(--blue);display:flex;padding-left:63px;border-bottom:3px solid #0f5e9c}
.nav a{color:var(--white);font-family:"Noticia Text",serif;font-size:13px;text-decoration:none;padding:0 16px;line-height:46px}
.nav a.active{background:var(--blue-light)}
.arrow{top:330px;height:30px;background:var(--blue);color:var(--white);font-size:12px;display:flex;align-items:center;justify-content:center;gap:8px}
.arrow.prev{left:0;width:30px}
.arrow.next{left:1141px;width:59px}
.tag-blue{left:178px;top:475px;width:384px;height:38px;background:var(--blue);color:var(--white);font-family:"Noticia Text",serif;font-size:28px;padding-left:15px;line-height:38px}
.tag-dark{left:178px;top:514px;width:429px;height:56px;background:rgba(30,30,30,.85);color:var(--white);font-family:"Noticia Text",serif;font-size:29px;padding-left:15px;line-height:56px}

/* form */
.enquiry{left:709px;top:170px;width:341px;height:533px;background:rgba(255,255,255,.96);box-shadow:0 1px 6px rgba(0,0,0,.25);padding:18px 30px 0}
.enquiry h2{font-family:"Noticia Text",serif;font-weight:400;font-size:21px;text-align:center;color:#333}
.enquiry .sub{font-size:12px;text-align:center;color:#666;margin-top:6px;margin-bottom:17px}
.field{height:32px;border:1px solid #ccc;border-radius:2px;font-family:"Noticia Text",serif;font-size:11px;color:#999;padding:0 12px;line-height:30px;margin-bottom:11px;background:var(--white)}
.label{font-family:"Noticia Text",serif;font-size:11px;color:#555;padding-left:12px;margin:-4px 0 11px}
.field.select{position:relative}
.field.select i{position:absolute;right:5px;top:4px;width:12px;height:22px;border:1px solid #bbb}
.field.area{height:72px;line-height:15px;padding-top:8px}
.submit{margin-top:22px;height:38px;background:var(--green-btn);color:var(--white);font-family:"Noticia Text",serif;font-size:16px;text-align:center;line-height:38px}

/* strip */
.strip{left:0;top:648px;width:1200px;height:104px;background:linear-gradient(#fafafa,#eee);border-bottom:1px solid #ddd}
.strip .k{left:177px;top:20px;font-size:12px;color:var(--green)}
.strip .s{left:177px;top:38px;font-size:12px;color:#666}
.strip .c{left:177px;top:64px;font-family:"Noticia Text",serif;font-size:16px;color:#333}

/* sections */
.title{left:174px;width:855px;display:flex;align-items:center;gap:16px;font-size:18px;color:#333;text-transform:uppercase}
.title::before,.title::after{content:"";flex:1;height:4px;border-top:1px solid var(--rule);border-bottom:1px solid var(--rule)}
.lead{left:175px;top:836px;width:852px;font-size:10.6px;line-height:17.6px;text-align:center;color:#666}
.lead b{font-weight:600;color:#444}
.more{color:var(--green);font-size:12px}
.frame{border:1px solid #ddd;padding:5px;background:#f7f7f7;box-shadow:0 1px 3px rgba(0,0,0,.1)}
.frame div{width:100%;height:100%}
.about-text{left:579px;top:1056px;width:446px;font-size:10.6px;line-height:17.6px;color:#666}
.about-text p{margin-bottom:18px}
.card{width:252px;text-align:center}
.card .frame{height:148px}
.card h3{font-weight:600;font-size:14.5px;color:#222;margin:28px 0 12px}
.card p{font-size:10.6px;line-height:16px;color:#777;padding:0 18px}
.card .more{display:block;margin-top:10px;font-size:11px}

/* lower band */
.lower{left:0;top:2011px;width:1200px;height:298px;background:var(--band);border-top:1px solid #e6e6e6;border-bottom:1px solid #e6e6e6}
.colhead{top:2044px;font-size:15px;color:#333;display:flex;align-items:center;gap:12px}
.colhead::before,.colhead::after{content:"";flex:1;border-top:1px solid var(--rule)}
.res-cap{left:180px;top:2230px;width:253px;height:30px;background:rgba(20,20,20,.8);color:var(--white);font-size:12px;line-height:30px;padding-left:14px}
.date{left:472px;width:60px;height:85px;background:#e6e6e6;text-align:center;color:#999;font-size:18px;padding-top:12px;line-height:1}
.date b{display:block;font-weight:400;font-size:36px;margin-top:4px}
.post{left:558px;width:152px;font-size:9.8px;line-height:14.5px;color:#777}
.post .by{margin-top:12px;color:#555}
.post .by b{font-weight:600}
.avatar{left:742px;width:78px;height:78px;border-radius:50%;border:5px solid #e4e4e4;background:radial-gradient(circle,#cbbfb2,#8d8276)}
.quote{left:820px;width:206px;background:#e9e9e9;font-size:9.4px;line-height:15px;color:#555;padding:8px 12px 8px 32px;position:absolute}
.quote::before{content:"\201C";position:absolute;left:12px;top:0;font-size:24px;color:#888;font-family:"Noticia Text",serif}
.quote .who{text-align:right}

/* footer */
.footer{left:0;top:2360px;width:1200px;height:154px;background:var(--dark);text-align:center;color:#bbb}
.footer .links{margin-top:25px;font-size:10px;line-height:17px}
.footer .links span{margin:0 12px}
.footer .copy{margin-top:36px;font-size:9.5px;color:#888;line-height:16px}
</style>
</head>
<body>

<div class="abs hero-photo" role="img" aria-label="Smiling lawyer in front of colleagues in an office"></div>
<header class="abs header"></header>
<div class="abs brand">Harwood &amp; Beale LLP</div>
<div class="abs social" aria-label="Social links"><span></span><span></span><span></span><span></span></div>
<nav class="abs nav">
  <a class="active">HOME</a><a>ABOUT US</a><a>RESULTS &amp; VERDICTS</a><a>SERVICES</a><a>BLOG</a><a>FAQS</a><a>LAWS</a><a>CONTACT US</a>
</nav>
<div class="abs arrow prev">&lt;</div>
<div class="abs arrow next">next <span>&gt;</span></div>
<div class="abs tag-blue">Defective Products Lawyers</div>
<div class="abs tag-dark">PRODUCTS LIABILITY LAW</div>

<div class="abs strip">
  <div class="abs k">DEFECTIVE PRODUCTS ATTORNEYS</div>
  <div class="abs s">Our defective products attorneys believe you !</div>
  <div class="abs c">Contact us for a free consultation now!
    <svg width="30" height="12" viewBox="0 0 30 12" style="vertical-align:middle;margin-left:8px"><path d="M2 9 Q14 5 27 4 M22 1 L27 4 L23 8" fill="none" stroke="#555" stroke-width="1.2"/></svg>
  </div>
</div>

<form class="abs enquiry">
  <h2>Enquiry Form</h2>
  <div class="sub">How Can We Help You?</div>
  <div class="field">Name*</div>
  <div class="field">Telephone number*</div>
  <div class="field">Email*</div>
  <div class="field">Address*</div>
  <div class="label">Country*:</div>
  <div class="field select"><i></i></div>
  <div class="field area">Please tell any details about the settlement or judgment that we may need to know</div>
  <div class="field">Your Query:</div>
  <div class="submit">Submit Form</div>
</form>

<h2 class="abs title" style="top:798px;font-weight:400">Harwood &amp; Beale LLP Experts</h2>
<p class="abs lead"><b>Lorem Ipsum is simply dummy text of the printing and typesetting industry.</b> Lorem Ipsum has been the industry's standard dummy text ever since the 1500s, when an unknown printer took a galley of type and scrambled it to make a type specimen book. It has survived not only five centuries, but also the leap into electronic typesetting, remaining essentially unchanged. It was popularised in the 1960s with the release of Typeline sheets containing Lorem Ipsum passages, and more recently with desktop publishing software like PageForge including versions of Lorem Ipsum.</p>
<div class="abs more" style="left:572px;top:920px">Read more</div>

<h2 class="abs title" style="top:976px;font-weight:400">Defective Products Lawyers</h2>
<div class="abs frame" style="left:180px;top:1057px;width:374px;height:221px"><div role="img" aria-label="Legal team meeting around a glass conference table" style="background:linear-gradient(180deg,#b8c6d2,#8aa0b3 55%,#6b7d8c)"></div></div>
<div class="abs about-text">
  <p>As a patient, you trust the manufacturers of products designed to enhance your health and well-being. Medical devices such as pacemakers, heart valves and artificial hips should be safe for your body and help you lead a normal, fulfilling life.</p>
  <p>When you undergo major surgery to have a medical device implanted, you trust that the device will function properly and last for the duration of your life. However, this does not always happen. When a medical device breaks or malfunctions, it can result in serious injury and wrongful death. At The Marlow Firm, our lawyers understand how difficult it is to accept an injury or death because of a faulty medical device. We believe that the manufacturers of these defective devices must be held accountable for any negligent and reckless behavior.</p>
  <div class="more" style="margin-top:-6px;font-size:13px">Read more</div>
</div>

<h2 class="abs title" style="top:1327px;font-weight:400">Why Choose Harwood &amp; Beale LLP</h2>

<div class="abs card" style="left:206px;top:1387px"><div class="frame"><div role="img" aria-label="Lawyers reviewing documents at a meeting" style="background:linear-gradient(#c3d0db,#8ea3b4)"></div></div><h3>Car defects recall lawyers</h3><p>Lorem Ipsum is simply dummy text of the printing and typesetting industry. Lorem Ipsum has been the industry's.</p><span class="more">Read more</span></div>
<div class="abs card" style="left:475px;top:1387px"><div class="frame"><div role="img" aria-label="Team stacking hands together" style="background:linear-gradient(135deg,#e3cbb8,#b98f76 60%,#4a4e5a)"></div></div><h3 style="margin-top:24px">Well-funded team</h3><p>Lorem Ipsum is simply dummy text of the printing and typesetting industry. Lorem Ipsum has been the industry's.</p><span class="more">Read more</span></div>
<div class="abs card" style="left:745px;top:1387px"><div class="frame"><div role="img" aria-label="Wooden judge's gavel" style="background:radial-gradient(circle at 35% 45%,#8a4e2a,#c99a6e 60%,#e3c9a6)"></div></div><h3 style="margin-top:24px">Defective Devices</h3><p>Lorem Ipsum is simply dummy text of the printing and typesetting industry. Lorem Ipsum has been the industry's.</p><span class="more">Read more</span></div>

<div class="abs card" style="left:206px;top:1690px"><div class="frame"><div role="img" aria-label="Attorneys working at a desk with a laptop" style="background:linear-gradient(#e8e4dc,#a8b7c6 60%,#5c6470)"></div></div><h3>Professional attorneys</h3><p>Lorem Ipsum is simply dummy text of the printing and typesetting industry. Lorem Ipsum has been the industry's.</p><span class="more">Read more</span></div>
<div class="abs card" style="left:475px;top:1690px"><div class="frame"><div role="img" aria-label="Handcuffed hands beside a gavel" style="background:radial-gradient(circle at 50% 40%,#c08a62,#6b3a1e 70%,#3a2012)"></div></div><h3 style="margin-top:26px">Criminal Defense</h3><p>Lorem Ipsum is simply dummy text of the printing and typesetting industry. Lorem Ipsum has been the industry's.</p><span class="more">Read more</span></div>
<div class="abs card" style="left:745px;top:1690px"><div class="frame"><div role="img" aria-label="Injured cyclist sitting on a park road" style="background:linear-gradient(#9aa48e,#8c8c86 50%,#6f706c)"></div></div><h3>Personal Injury</h3><p>Lorem Ipsum is simply dummy text of the printing and typesetting industry. Lorem Ipsum has been the industry's.</p><span class="more">Read more</span></div>

<section class="abs lower"></section>
<h3 class="abs colhead" style="left:176px;width:262px;font-weight:400">Resources</h3>
<h3 class="abs colhead" style="left:472px;width:240px;font-weight:400">Blog</h3>
<h3 class="abs colhead" style="left:742px;width:284px;font-weight:400">Testimonial</h3>

<div class="abs frame" style="left:174px;top:2086px;width:264px;height:209px;padding:3px"><div role="img" aria-label="Constitution document with a gavel in black and white" style="background:linear-gradient(135deg,#e6e6e6,#9a9a9a 50%,#3c3c3c)"></div></div>
<div class="abs res-cap">Harwood &amp; Beale LLP Recovery Resources</div>

<div class="abs date" style="top:2090px">Nov<b>20</b></div>
<div class="abs post" style="top:2096px">If you have finally gotten to the end of your legal road and been awarded a judgment..<div class="by">by <b>Tessa Vaughn</b></div></div>
<div class="abs date" style="top:2185px">Jun<b>18</b></div>
<div class="abs post" style="top:2192px">Unlike "collection agencies" - who are great for small claims - we focus..<div class="by">by <b>Milo Hart</b></div></div>

<div class="abs avatar" style="top:2088px" role="img" aria-label="Client portrait"></div>
<div class="quote" style="top:2096px">The euphoria of winning a judgment in small claims or municipal.<div class="who">- Clara Dunmore</div></div>
<div class="abs avatar" style="top:2180px" role="img" aria-label="Client portrait"></div>
<div class="quote" style="top:2188px">If the debtor doesn't pay voluntarily, you must somehow collect.<div class="who">- Owen Pryce</div></div>

<footer class="abs footer">
  <div class="links">Home<span>|</span>About us<span>|</span>Results &amp; Verdicts<span>|</span>Services<span>|</span>Blog<br>Faqs<span>|</span>Laws<span>|</span>Contact Us</div>
  <div class="copy">COPYRIGHT 2014 Harwood &amp; Beale LLP<br>This information is not to be interpreted as providing legal services, nor as proposing any form of legal advice.</div>
</footer>

</body>
</html>
```